Business Card Design and a letter head logo

50/50 share milker dairy farmer of 400 cows with a silage and haymaking sideline business
15 years farming currently looking for new opportunities within the dairy farming sector. trying to put together a portfolio to get another 50/50 share milking job aswell

Industry/Entity Type

Farming

Contact Information for Business Card

Brindle Farming LTD
Corwin & Lisette Pargeter
263 Kellow Ridge Highway
RD4 Tepuhina 0382
Whangarei
pargeter.corwin@fernmail.example.nz
0274381926
(09) 5817342

```html
<!DOCTYPE html>
<html lang="en">
<head>
<meta charset="utf-8">
<title>Brindle Farming LTD – Business Card</title>
<link href="https://fonts.googleapis.com/css2?family=Saira+Condensed:wght@300;400;700&display=swap" rel="stylesheet">
<style>
  :root {
    --page: #e8e6e2;
    --card: #ffffff;
    --card-edge: #f1f1f1;
    --ink: #1c1c1c;
    --ink-soft: #444444;
    --rule: #2a2a2a;
    --rule-fade: rgba(42,42,42,0);
  }
  * { box-sizing: border-box; margin: 0; padding: 0; }
  html, body {
    width: 1200px; height: 892px; overflow: hidden;
    background: var(--page);
    font-family: "Saira Condensed", "Arial Narrow", sans-serif;
    color: var(--ink);
  }
  .stage {
    width: 1200px; height: 892px;
    display: flex; align-items: center; justify-content: center;
  }
  .business-card {
    position: relative;
    width: 980px; height: 560px;
    background: linear-gradient(135deg, var(--card) 0%, var(--card-edge) 100%);
    box-shadow: 0 2px 10px rgba(0,0,0,0.12);
    display: flex;
  }
  .brand-panel {
    width: 470px; height: 100%;
    display: flex; align-items: center; justify-content: center;
    position: relative;
  }
  .brand-frame {
    position: relative;
    padding: 40px 0;
    display: flex; align-items: center; gap: 22px;
  }
  .brand-frame::before, .brand-frame::after {
    content: ""; position: absolute; left: 0; right: 0; height: 3px;
    background: var(--rule);
  }
  .brand-frame::before { top: 0; }
  .brand-frame::after { bottom: 0; }
  .brand-square {
    width: 46px; height: 46px; background: var(--ink);
  }
  .brand-name {
    font-weight: 700; font-size: 58px; line-height: 0.95;
    letter-spacing: 1px; color: var(--ink);
  }
  .divider {
    position: absolute; left: 470px; top: 40px; bottom: 40px; width: 3px;
    background: linear-gradient(to bottom, var(--rule-fade), var(--rule) 35%, var(--rule) 65%, var(--rule-fade));
  }
  .contact-panel {
    flex: 1; padding: 90px 60px 0 80px;
  }
  .person-name {
    font-weight: 300; font-size: 46px; letter-spacing: 0.5px; line-height: 1.1;
  }
  .person-role {
    font-weight: 300; font-size: 20px; color: var(--ink-soft); margin: 2px 0 0 4px;
  }
  .contact-list {
    list-style: none; margin-top: 52px;
    font-weight: 300; font-size: 25px; line-height: 1.25;
  }
  .contact-item { display: flex; align-items: flex-start; gap: 14px; margin-bottom: 6px; }
  .contact-icon { width: 18px; height: 18px; margin-top: 7px; flex: none; fill: var(--ink); }
</style>
</head>
<body>
<main class="stage">
  <article class="business-card">
    <section class="brand-panel">
      <div class="brand-frame">
        <span class="brand-square"></span>
        <h1 class="brand-name">Brindle<br>Farming<br>LTD</h1>
      </div>
    </section>
    <div class="divider"></div>
    <section class="contact-panel">
      <h2 class="person-name">Corwin &amp; Lisette Pargeter</h2>
      <p class="person-role">owner</p>
      <ul class="contact-list">
        <li class="contact-item">
          <svg class="contact-icon" viewBox="0 0 24 24" aria-hidden="true"><path d="M6.6 10.8c1.4 2.8 3.8 5.2 6.6 6.6l2.2-2.2c.3-.3.7-.4 1-.2 1.1.4 2.3.6 3.6.6.6 0 1 .4 1 1V20c0 .6-.4 1-1 1C10.6 21 3 13.4 3 4c0-.6.4-1 1-1h3.5c.6 0 1 .4 1 1 0 1.3.2 2.5.6 3.6.1.3 0 .7-.2 1z"/></svg>
          <span>0274381926</span>
        </li>
        <li class="contact-item">
          <svg class="contact-icon" viewBox="0 0 24 24" aria-hidden="true"><path d="M6.6 10.8c1.4 2.8 3.8 5.2 6.6 6.6l2.2-2.2c.3-.3.7-.4 1-.2 1.1.4 2.3.6 3.6.6.6 0 1 .4 1 1V20c0 .6-.4 1-1 1C10.6 21 3 13.4 3 4c0-.6.4-1 1-1h3.5c.6 0 1 .4 1 1 0 1.3.2 2.5.6 3.6.1.3 0 .7-.2 1z"/></svg>
          <span>(09) 5817342</span>
        </li>
        <li class="contact-item">
          <svg class="contact-icon" viewBox="0 0 24 24" aria-hidden="true"><path d="M2 5h20v14H2z M4 7v.5l8 5 8-5V7z" fill-rule="evenodd"/></svg>
          <span>pargeter.corwin@fernmail.example.nz</span>
        </li>
        <li class="contact-item">
          <svg class="contact-icon" viewBox="0 0 24 24" aria-hidden="true"><path d="M12 2a7 7 0 0 0-7 7c0 5 7 13 7 13s7-8 7-13a7 7 0 0 0-7-7zm0 9.5A2.5 2.5 0 1 1 12 6.5a2.5 2.5 0 0 1 0 5z"/></svg>
          <span>263 Kellow Ridge Highway RD4<br>Tepuhina 0382 Whangarei</span>
        </li>
      </ul>
    </section>
  </article>
</main>
</body>
</html>
```